Business Card for Makeup Artist

I need a business card designed for my makeup and hair artistry business which is primarily events and weddings focused. The card needs to be sleek, simple, stylish and appealing to women. I would prefer a white background but open to suggestions also. I also love the marble background look. I have attached some example pics. It needs to be a double sided card with logo and/or design on one side and contact details in the centre of the card on the other side. NO LOGO ON BACK. Examples attached.

Target Market(s)

Females age 14-55

Industry/Entity Type

Business

Contact Information for Business Card

Nora Vint
Principal Makeup Artist
P: 0413 925 214
E: nora@lumirabeauty.com.au
W: www.lumirabeauty.com.au

Requirements
Should not have
• No yellow, green, red or blue in the design.

```html
<!DOCTYPE html>
<html lang="en">
<head>
<meta charset="UTF-8">
<title>Lumira Makeup Artistry – Business Card</title>
<link rel="stylesheet" href="https://fonts.googleapis.com/css2?family=Josefin+Sans:wght@300;400&family=Sofia&display=swap">
<style>
  :root {
    --stage: #e9e8ea;
    --orchid: #d966a8;
    --pearl-light: #f4f4f7;
    --pearl-mid: #dfdfe6;
    --charcoal: #5a5a5c;
    --white: #ffffff;
  }
  * { margin: 0; padding: 0; box-sizing: border-box; }
  html, body {
    width: 1200px;
    height: 800px;
    overflow: hidden;
    background: var(--stage);
  }
  .canvas {
    position: relative;
    width: 1200px;
    height: 800px;
    display: flex;
    align-items: center;
    justify-content: center;
    gap: 60px;
  }
  .card {
    position: relative;
    width: 520px;
    height: 297px;
    border-radius: 3px;
    box-shadow: 0 6px 18px rgba(0, 0, 0, 0.12);
    overflow: hidden;
  }

  /* Front */
  .card-front { background: var(--pearl-light); }
  .pearl-texture {
    position: absolute;
    inset: 0;
    background:
      radial-gradient(circle at 25% 30%, var(--pearl-mid) 0%, transparent 45%),
      radial-gradient(circle at 75% 70%, var(--pearl-mid) 0%, transparent 50%),
      var(--pearl-light);
  }
  .rule {
    position: absolute;
    height: 2px;
    background: var(--orchid);
  }
  .rule-top { top: 52px; left: 104px; width: 260px; }
  .rule-bottom { bottom: 52px; right: 78px; width: 260px; }
  .brand {
    position: absolute;
    inset: 0;
    display: flex;
    align-items: center;
    justify-content: center;
    gap: 12px;
  }
  .brand-dot {
    width: 12px;
    height: 12px;
    border-radius: 50%;
    background: var(--orchid);
  }
  .brand-name {
    font-family: "Josefin Sans", sans-serif;
    font-weight: 400;
    font-size: 26px;
    letter-spacing: 0.08em;
    color: var(--charcoal);
    text-transform: uppercase;
  }

  /* Back */
  .card-back {
    background: var(--orchid);
    color: var(--white);
    text-align: center;
  }
  .holder-name {
    position: absolute;
    top: 74px;
    left: 0;
    right: 0;
    font-family: "Sofia", cursive;
    font-size: 50px;
    line-height: 1;
  }
  .holder-title {
    position: absolute;
    top: 140px;
    left: 0;
    right: 0;
    font-family: "Josefin Sans", sans-serif;
    font-weight: 300;
    font-size: 19px;
    letter-spacing: 0.02em;
  }
  .contact-line {
    position: absolute;
    bottom: 26px;
    left: 0;
    right: 0;
    display: flex;
    justify-content: center;
    align-items: center;
    font-family: "Josefin Sans", sans-serif;
    font-weight: 300;
    font-size: 12.5px;
    list-style: none;
  }
  .contact-line li + li::before {
    content: "";
    display: inline-block;
    width: 1px;
    height: 14px;
    background: var(--white);
    margin: 0 12px;
    vertical-align: -2px;
  }
</style>
</head>
<body>
  <main class="canvas">
    <section class="card card-front" aria-label="Card front">
      <div class="pearl-texture" role="img" aria-label="Soft pearl-white mottled marble texture"></div>
      <span class="rule rule-top"></span>
      <span class="rule rule-bottom"></span>
      <div class="brand">
        <span class="brand-dot"></span>
        <span class="brand-name">Lumira Makeup Artistry</span>
      </div>
    </section>

    <section class="card card-back" aria-label="Card back">
      <h1 class="holder-name">Nora Vint</h1>
      <p class="holder-title">Principal Makeup Artist</p>
      <ul class="contact-line">
        <li>nora@lumirabeauty.com.au</li>
        <li>0413 925 214</li>
        <li>www.lumirabeauty.com.au</li>
      </ul>
    </section>
  </main>
</body>
</html>
```